!! Innovative new tea company needs packaging design !!

** NB. We need this project as a starting point for our company. We would like to/ intend to have an ongoing relationship with the designer to add to/ change and develop the design in the future on freelance basis pending available workload.

We are in the process of creating a range of functional wellness drinks based on green tea - company name k~. We will have a range of drinks based on green tea attributed to functional effects - boost, detox, immunity etc. Aim of the company is to create a healthy, modern, vibrant company that offers a range of drinks that offer healthy wellness properties, in great tasting fruit flavours.

We need packaging design for the boxes, initially for tea bags. dimensions will be Length – 12cm, Width – 6.75cm, Height – 7.75cm ( please note this means that the box will be TALL / UPRIGHT STANDING)

The brand name is k~ ( to represent green tea + other ingredients / effects). Four initial tea's will be produced that we need to show packaging for :

k~ boost ( rasberry & pomegranite flavour )
k~ immunity ( orange & blueberry )
k~ detox ( apple & blackcurrant )
k~ multi vitamin ( lemon & peach )

We have had the below central brand logo and individual tea logo edits produced already, attached below.

*****Please note we intend the 4 packages to be the same consistent design - only change is on the title of each. For that reason we ONLY REQUEST TO SEE ONE DESIGN ON ONE PRODUCT from a designer to agree on format. Once agreed we will then request you give us the other 3 on agreed format ******

We are aiming to be a very young, vibrant company aiming at the 20 - 40 health conscious consumer. Were taking inspiration from companies like Quillow smoothies and leaf owls and want branding to be in line with those themes.PLEASE LOOK THIS UP TO UNDERSTAND. We need box designs to be completed. Ideally building on the below designs weve had commissioned. However, if a better suggestion on the logo , or a tweak to these will improve the design then we are very much open to it.

Packaging must be, clear white background and bold colors along the line of each flavour teas colour ( ie red for boost, yellow multi vitamin etc). We would ideally like the top and one side ( ONLY ) of the box to be coloured background ( matching the drink colour ). We are wanting simple and clear design FAIRLY MINIMALIST to convey the point of the brand to be simple clear and healthy ingredients. At the same time it must clearly stand out on a shelf. Lighthearted and not too serious, ideally simple, fun illustrated drawings ( ideally outlines/very simple drawings) of the fruit aligned to each flavour and any other branding / mascot logo design that you can suggest.

Also possible cartoon/simple illustration tea leaf somewhere on the box.

We need packaging for the 4 teas - 1 consistent design and theme, with only changes to color and a few illustrations per box.

Please note - We want text font to be funky, friendly, soft - various sizes on the text on the boxes - NOT everything the same size and generic font.

text to go on the box

( front of box):

- main t+boost/immunity etc logo
.(tagline underneath) Wellness drinks

- * Green tea with vitamins drink

- * Natural Ceylon green tea with added vitamins and herbs to give you the best start to your day.

- * 5 reasons to drink this!!
100% natural ingredients
x% of your RDA of x
x mg of antioxidants to keep your heart healthy.
Naturally sweet taste
only x calories per cup!

(side of box)

Ingredients

We use only the finest hand picked ceylon green tea and mix it with natural fruit pieces, a hint of natural flavouring as our base. We add the goodness of burdock root and echinacea to help build your body's defenses and sweeten it with a dash of the south american stevia leaf to give a great tasting drink that will do you some good!

( side of box )

Nutrition Facts

Serving Size: 1 tea bag (4g)

Makes: 8 fl. oz.

Servings Per Container: 25

Amount Per Serving
Calories 0

% Daily Value*
Total Fat 0g
0%
Sodium 0mg
5%
Total Carb. 0g
0%
Sugars 10g
Protein 0g

* Percent Daily Values are based on a 2,000 calorie diet.

The above is how we forsee the packaging for now. However - anything that you can reccommend that is innovative to help us stand out to a young , trendy audience will be welcome.

Please message with any questions or comments.
Updates

Dear All - Please note - we have updated the brief with the packaging die line for your reference. Please note the box will be upstanding so designs should accomodate for a tall box.

Dear All - To reiterate key points of the brief - We request the deign to be stand out here. Majority white background with splashes/swirls/blotches of colour ( whatever design suggested ).Further to that, illustrations ( drawings - not pictures ) of fruit / tea leaves to stay in line with young, funky image. 

Overall theme is young, bright and modern - we need the packaging to reflect this. Not just standard text font and background colouring.
Any more clarity needed please contact us. 

Reason: Dear All We have increased the budget for this project and extended the deadline by additional 7 days. To date we have not received the designs we are happy with so want to give all added time to revise - follow the brief - and resubmit. Due to quality of designs received so far - we will not guarantee payment yet - HOWEVER - Intention is to get this completed for the business by next week latest- for that reason, as soon as someone has submitted a design that is at least along the right lines - we will then move to guarantee payment. Please also note - we intend to / hope to work with the designer directly on ongoing projects for the company so want a good - long term relationship from this. Good luck and please contact us if any more information needed. Regards

Dear all

Please can we request that for the sides of the box with a white background - text is in a green colour ( same shade as the original k~ logo green ). We would like this to be our standard font colour against white background. 

Obviously, please add colour where you see fit but we want a clean , consistent font across the boxes and eventually our web site. 

For the coloured backgrounds of the side and top - will leave up to you whatever colour font looks best. 

Reason: Deadline extended to provide some more feedback to designers. No decision yet made.

Target Market(s)

Young, health conscious individuals.

Industry/Entity Type

It Company

```html
<!DOCTYPE html>
<html lang="en">
<head>
<meta charset="UTF-8">
<title>k~ multi vitamin – lemon &amp; peach tea box</title>
<link rel="stylesheet" href="https://fonts.googleapis.com/css2?family=Nunito:wght@300;400;700;800&display=swap">
<style>
  :root {
    --canvas: #ffffff;
    --yellow: #f2c100;
    --yellow-deep: #d6a400;
    --paper: #f1f1f1;
    --side-grey: #8c8c8c;
    --side-ink: #2b2b2b;
    --title-green: #b9c400;
    --brand-red: #d9261c;
    --leaf-pale: #f4ecd0;
    --cream: #fbeec2;
  }
  * { box-sizing: border-box; margin: 0; padding: 0; }
  html, body {
    width: 1200px; height: 800px; overflow: hidden;
    background: var(--canvas);
    font-family: "Nunito", sans-serif;
  }
  .dieline { position: relative; width: 1200px; height: 800px; }

  /* top panel */
  .panel-top {
    position: absolute; left: 460px; top: 20px; width: 300px; height: 170px;
    background: var(--paper);
    overflow: hidden;
  }
  .panel-top .top-blob {
    position: absolute; left: 30px; top: 18px; width: 240px; height: 134px;
    border-radius: 50%;
    background: var(--yellow-deep);
    display: flex; align-items: center; justify-content: center; gap: 10px;
  }
  .brand-mark { display: flex; align-items: center; gap: 8px; }
  .brand-mark .dot {
    width: 22px; height: 22px; border-radius: 50%;
  }
  .brand-mark .name { font-weight: 800; line-height: 1; }
  .top-blob .dot { background: var(--brand-red); }
  .top-blob .name { color: var(--brand-red); font-size: 46px; }

  /* front panel */
  .panel-front {
    position: absolute; left: 460px; top: 190px; width: 300px; height: 570px;
    background: var(--paper);
    overflow: hidden;
  }
  .front-colour { position: absolute; inset: 0; }
  .product-title {
    position: absolute; left: 62px; top: 430px;
    transform: rotate(-90deg); transform-origin: left top;
    font-size: 40px; font-weight: 700; color: var(--title-green);
    white-space: nowrap; letter-spacing: 0.5px;
  }
  .front-brand {
    position: absolute; left: 18px; top: 420px;
  }
  .front-brand .dot { background: var(--title-green); width: 18px; height: 18px; }
  .front-brand .name { color: var(--title-green); font-size: 40px; }
  .leaf-art {
    position: absolute; left: 150px; top: 200px; width: 110px; height: 230px;
    border-radius: 50% 50% 50% 50% / 60% 60% 40% 40%;
    background: var(--leaf-pale);
  }
  .flavour {
    position: absolute; left: 24px; bottom: 22px; line-height: 1;
  }
  .flavour .fruit-one { display: block; font-size: 42px; font-weight: 300; color: var(--paper); }
  .flavour .fruit-two { display: block; font-size: 36px; font-weight: 800; color: var(--cream); margin-top: 2px; }

  /* side panel */
  .panel-side {
    position: absolute; left: 260px; top: 190px; width: 200px; height: 570px;
    background: var(--side-grey);
    color: var(--side-ink);
    padding: 26px 18px;
    font-size: 10px; line-height: 1.35;
  }
  .ingredients h2 { font-size: 11px; font-weight: 800; margin-bottom: 8px; }
  .ingredients p { font-weight: 700; }
  .cup-icon { display: block; margin: 34px auto 22px; }
  .nutrition { font-weight: 700; }
  .nutrition p { margin-bottom: 6px; }
  .nutrition table { border-collapse: collapse; margin-top: 10px; font-size: 9px; }
  .nutrition td { padding: 1px 10px 1px 0; }
  .side-brand {
    position: absolute; left: 18px; bottom: 24px;
  }
  .side-brand .dot { background: var(--brand-red); width: 14px; height: 14px; }
  .side-brand .name { color: var(--brand-red); font-size: 24px; }
</style>
</head>
<body>
<main class="dieline">

  <section class="panel-top">
    <div class="top-blob">
      <div class="brand-mark"><span class="dot"></span><span class="name">k~</span></div>
    </div>
  </section>

  <section class="panel-side">
    <div class="ingredients">
      <h2>Ingredients:</h2>
      <p>We blend hand picked green tea with natural fruit pieces and a hint of flavour, then add burdock root and echinacea, sweetened with a dash of stevia leaf for a drink that does you good.</p>
    </div>
    <svg class="cup-icon" width="34" height="36" viewBox="0 0 34 36" aria-hidden="true">
      <path d="M10 2c-2 3 2 4 0 7M16 2c-2 3 2 4 0 7" stroke="#1a1a1a" stroke-width="2" fill="none"/>
      <path d="M3 12h22v14a8 8 0 0 1-8 8h-6a8 8 0 0 1-8-8z" fill="#1a1a1a"/>
      <path d="M25 15h3a4 4 0 0 1 0 9h-3" stroke="#1a1a1a" stroke-width="3" fill="none"/>
    </svg>
    <div class="nutrition">
      <p>Serving Size: 1 tea bag (4g)</p>
      <p>Makes: 8 fl. oz.</p>
      <p>Servings Per Container: 25</p>
      <table>
        <tr><td>Calories</td><td>0</td></tr>
        <tr><td>Total Fat</td><td>0g</td></tr>
        <tr><td>Sodium</td><td>0mg</td></tr>
        <tr><td>Carb.</td><td>0g</td></tr>
        <tr><td>Protein</td><td>0g</td></tr>
      </table>
    </div>
    <div class="brand-mark side-brand"><span class="dot"></span><span class="name">k~</span></div>
  </section>

  <section class="panel-front">
    <svg class="front-colour" width="300" height="570" viewBox="0 0 300 570" aria-hidden="true">
      <path d="M0 0H300V570H0V450H130C130 380 150 320 150 260C150 200 110 160 150 110C180 70 170 30 110 20C60 12 20 20 0 40Z" fill="var(--yellow)"/>
      <path d="M0 0H210C200 30 170 36 130 30C80 22 30 28 0 50Z" fill="var(--yellow-deep)"/>
    </svg>
    <div class="leaf-art" role="img" aria-label="Simple drawn tea leaf"></div>
    <h1 class="product-title">multi vitamin</h1>
    <div class="brand-mark front-brand"><span class="dot"></span><span class="name">k~</span></div>
    <p class="flavour"><span class="fruit-one">lemon</span><span class="fruit-two">&amp; peach</span></p>
  </section>

</main>
</body>
</html>
```